MapleTideEvents
MaplTideEvents - Business Card/Stationary
I need double sided standard sized Business Card [3.5" x 2"]
we use "segan" on the website - feel free to expirement, we are not set on one yet
Professional
Nadia Feltwick
Director of Logistics
4187 Birchwell Hollow Lane
Larkmoor, OR 95182
nadia@mapletide.com
www.mapletide.com
-Please look at our website: www.mapletide.com
We would like the business card to replicate the look of the website.
-As noted earlier, we have not settled on a font yet, please feel free to be creative with the styles
- Font used on website = segan (or similar)
-Double-Sided is "optional" we would also like to see just some single sided versions as well.
- Regular standard size business card
we wanted to explore the option of having a double sided card. This is not mandatory, but if there is a creative design for it, this would be great.
Logo - Icon ONLY
Logo - Icon with Title

```html
<!DOCTYPE html>
<html lang="en">
<head>
<meta charset="utf-8">
<title>MapleTideEvents – Business Card Set</title>
<link rel="stylesheet" href="https://fonts.googleapis.com/css2?family=Tinos:wght@400;700&family=Open+Sans:wght@600&display=swap">
<style>
  :root {
    --page: #eceae6;
    --label: #3a3a3a;
    --blue-light: #5cb8ec;
    --blue-mid: #2a93d8;
    --blue-deep: #0f6fb8;
    --white: #ffffff;
    --paper-shade: #e6e8ea;
    --ink: #4a4f55;
    --ink-soft: #7d848c;
    --name-blue: #1a7cc4;
  }
  * { box-sizing: border-box; margin: 0; padding: 0; }
  html, body { width: 1200px; height: 1057px; overflow: hidden; }
  body { background: var(--page); position: relative; font-family: "Tinos", "Times New Roman", serif; color: var(--ink); }

  .side-label { position: absolute; top: 22px; width: 230px; text-align: center; font-family: "Open Sans", Arial, sans-serif; font-weight: 600; font-size: 30px; color: var(--label); }

  .card { position: absolute; overflow: hidden; box-shadow: 0 4px 14px rgba(0,0,0,.22); }
  .card--portrait { width: 230px; height: 400px; top: 80px; }
  .card--landscape { width: 400px; height: 229px; }
  .card--blue { background: linear-gradient(160deg, var(--blue-light) 0%, var(--blue-mid) 55%, var(--blue-deep) 100%); color: var(--white); }
  .card--white { background: linear-gradient(160deg, var(--white) 0%, #f4f5f6 55%, var(--paper-shade) 100%); }

  .address { position: absolute; font-size: 10.5px; line-height: 1.45; white-space: nowrap; }
  .address p + p { margin-top: 7px; }

  .brand { position: absolute; display: flex; align-items: center; gap: 7px; font-size: 20px; font-weight: 700; letter-spacing: -.3px; white-space: nowrap; }
  .brand-square { width: 26px; height: 26px; flex: none; }
  .card--blue .brand { color: var(--white); }
  .card--blue .brand-square { background: var(--white); }
  .card--white .brand { color: var(--name-blue); }
  .card--white .brand-square { background: var(--blue-mid); }

  .person { position: absolute; white-space: nowrap; }
  .person-name { font-size: 15px; font-weight: 700; color: var(--name-blue); }
  .person-title { font-size: 10.5px; color: var(--ink-soft); margin-top: 2px; }
  .card--blue .person-onblue .person-name,
  .card--blue .person-onblue .person-title { color: var(--white); }

  .name-band { position: absolute; left: 0; right: 0; bottom: 0; height: 78px; background: var(--white); }

  .mark-block { position: absolute; left: 0; right: 0; text-align: center; }
  .mark-square { width: 40px; height: 40px; margin: 0 auto; }
  .card--white .mark-square { background: linear-gradient(150deg, var(--blue-light), var(--blue-deep)); }
  .card--blue .mark-square { background: var(--white); }
  .tagline { font-size: 9px; margin-top: 6px; color: var(--ink-soft); }
  .card--blue .tagline { color: var(--white); }
  .web { position: absolute; left: 0; right: 0; text-align: center; font-size: 13px; color: var(--ink-soft); }
  .card--blue .web { color: var(--white); }
</style>
</head>
<body>
  <div class="side-label" style="left:35px">Front</div>
  <div class="side-label" style="left:295px">Back</div>
  <div class="side-label" style="left:660px">Back</div>
  <div class="side-label" style="left:925px">Front</div>

  <section class="card card--portrait card--blue" style="left:35px">
    <div class="address" style="left:22px; top:22px">
      <p>4187 Birchwell Hollow Lane<br>Larkmoor, OR 95182</p>
      <p>Phone: (877) 555-0143<br>Email: nadia@mapletide.com<br>Web: www.mapletide.com</p>
    </div>
    <div class="brand" style="left:18px; top:232px"><span class="brand-square"></span>MapleTideEvents</div>
    <div class="name-band"></div>
    <div class="person" style="right:18px; bottom:22px; text-align:right">
      <div class="person-name">Nadia Feltwick</div>
      <div class="person-title">Director of Logistics</div>
    </div>
  </section>

  <section class="card card--portrait card--white" style="left:295px">
    <div class="mark-block" style="top:292px">
      <div class="mark-square"></div>
      <div class="tagline">shaping your moment</div>
    </div>
    <div class="web" style="bottom:22px">www.mapletide.com</div>
  </section>

  <section class="card card--portrait card--blue" style="left:660px">
    <div class="mark-block" style="top:292px">
      <div class="mark-square"></div>
      <div class="tagline">shaping your moment</div>
    </div>
    <div class="web" style="bottom:22px">www.mapletide.com</div>
  </section>

  <section class="card card--portrait card--white" style="left:925px">
    <div class="address" style="right:20px; top:22px; text-align:right">
      <p>4187 Birchwell Hollow Lane<br>Larkmoor, OR 95182</p>
      <p>Phone: (877) 555-0143<br>Email: nadia@mapletide.com<br>Web: www.mapletide.com</p>
    </div>
    <div class="brand" style="left:16px; top:232px"><span class="brand-square"></span>MapleTideEvents</div>
    <div class="person" style="right:18px; top:300px; text-align:right">
      <div class="person-name">Nadia Feltwick</div>
      <div class="person-title">Director of Logistics</div>
    </div>
  </section>

  <section class="card card--landscape card--blue" style="left:45px; top:530px">
    <div class="brand" style="left:22px; top:28px"><span class="brand-square"></span>MapleTideEvents</div>
    <div class="person person-onblue" style="right:22px; top:92px; text-align:right">
      <div class="person-name">Nadia Feltwick</div>
      <div class="person-title">Director of Logistics</div>
    </div>
    <div class="address" style="left:22px; top:92px">
      <p>4187 Birchwell Hollow Lane<br>Larkmoor, OR 95182</p>
      <p>Phone: (877) 555-0143<br>Email: nadia@mapletide.com<br>Web: www.mapletide.com</p>
    </div>
  </section>

  <section class="card card--landscape card--white" style="left:785px; top:530px">
    <div class="brand" style="left:22px; top:26px"><span class="brand-square"></span>MapleTideEvents</div>
    <div class="address" style="left:22px; top:96px">
      <p>4187 Birchwell Hollow Lane<br>Larkmoor, OR 95182</p>
      <p>Phone: (877) 555-0143<br>Email: nadia@mapletide.com<br>Web: www.mapletide.com</p>
    </div>
    <div class="person" style="right:22px; top:96px; text-align:right">
      <div class="person-name">Nadia Feltwick</div>
      <div class="person-title">Director of Logistics</div>
    </div>
  </section>

  <section class="card card--landscape card--white" style="left:130px; top:795px">
    <div class="mark-block" style="top:62px">
      <div class="mark-square"></div>
      <div class="tagline">shaping your moment</div>
    </div>
    <div class="web" style="top:130px">www.mapletide.com</div>
  </section>

  <section class="card card--landscape card--blue" style="left:685px; top:795px">
    <div class="mark-block" style="top:62px">
      <div class="mark-square"></div>
      <div class="tagline">shaping your moment</div>
    </div>
    <div class="web" style="top:130px">www.mapletide.com</div>
  </section>
</body>
</html>
```